Psychology practice Logo and Business card design

Still in its early development, Meridian Counselling Group provides comprehensive psychology services to a diverse range of clients in the Barossa Valley. Some details available on website - www.tallowmind-example.com.
The Barossa is a semi-rural area, famous for our wines.
At Meridian Counselling Group we work with young children, adolescents, families and adults. We will soon move into our own premises in a restored historic/heritage building in the main street of Angaston. This 1870s building was most recently a bookshop, but has previously been a grocer store and secret 'clubhouse'.
The preferred therapeutic style of our psychologist is called RFT therapy - this is in part how the name of the business was decided. We are also encouraging of clients' physical health in conjunction with their emotional health.
Updates

Thank you to those designers who have already provided early ideas.

A few extra thoughts:

- given the national psychology body is the NBT, I'm keen to avoid using that abbreviation;

- simple is best;

- I would prefer the business name to be the feature rather than my own name;

- a simple logo as part of the design would be fantastic so it can be adapted for signage etc.

Many thanks for your continued help.

Target Market(s)

broad - adults, adolescents, families.

Industry/Entity Type

Building

Contact Information for Business Card

Meridian Counselling Group
www. tallowmind-example.com

PO Box 714
Kellbrook SA 5291

Delia Farrant FNBT
Psychologist
BSc, Grad Dip Ed, M Psych (Clinical)
mob: 0431 957 284
fax: 0869 413 508
email: delia@tallowmind-example.com

Requirements
Must have
• Simple logo design included.
All contact information.
Reverse side for appointment details (Next appointment: Date, Time)
Nice to have
• Something representative of hope / future focus.
Possibly a combination of modern feel with connection to heritage?
Gender neutral colours
Should not have
• abbreviation to NBT
photograph

```html
<!DOCTYPE html>
<html lang="en">
<head>
<meta charset="utf-8">
<title>Meridian Counselling Group – Business Card</title>
<link rel="stylesheet" href="https://fonts.googleapis.com/css2?family=Open+Sans:ital,wght@0,400;0,600;1,400;1,600&display=swap">
<style>
  :root {
    --bg-light: #f1f1f1;
    --bg-mid: #cdcdcd;
    --card-dark: #2a2b2d;
    --card-darker: #1d1e20;
    --panel-light: #e2e2e2;
    --gold: #c9a135;
    --gold-bright: #e8d23f;
    --text-light: #ffffff;
    --text-muted: #d8d8d8;
    --text-dark: #222222;
  }
  * { box-sizing: border-box; margin: 0; padding: 0; }
  html, body {
    width: 1200px;
    height: 1000px;
    overflow: hidden;
  }
  body {
    background: radial-gradient(ellipse at 50% 45%, var(--bg-light) 0%, var(--bg-mid) 100%);
    font-family: "Open Sans", Arial, sans-serif;
    position: relative;
  }
  .card {
    position: absolute;
    top: 348px;
    width: 520px;
    height: 304px;
    overflow: hidden;
    box-shadow: 0 14px 30px rgba(0,0,0,0.18);
  }

  /* ---------- Appointment side ---------- */
  .card--back {
    left: 60px;
    background: var(--panel-light);
  }
  .back__header {
    position: absolute;
    top: 0; left: 0; right: 0;
    height: 78px;
    background: linear-gradient(160deg, var(--card-darker), var(--card-dark));
  }
  .back__tab {
    position: absolute;
    left: 0; top: 33px;
    width: 8px; height: 13px;
    background: var(--gold-bright);
  }
  .back__title {
    position: absolute;
    left: 17px; top: 25px;
    color: var(--text-light);
    font-style: italic;
    font-weight: 600;
    font-size: 21px;
    line-height: 28px;
  }
  .back__bar {
    position: absolute;
    left: 236px; right: 0; top: 33px;
    height: 13px;
    background: linear-gradient(90deg, var(--gold), var(--gold-bright));
  }
  .back__fields {
    position: absolute;
    left: 17px; top: 96px;
    list-style: none;
    color: var(--text-dark);
    font-size: 17px;
  }
  .back__fields li { height: 40px; }
  .back__footer {
    position: absolute;
    left: 0; right: 0; bottom: 0;
    height: 78px;
    background: linear-gradient(160deg, var(--card-dark), var(--card-darker));
    color: var(--text-light);
    font-size: 14px;
    text-align: center;
    line-height: 78px;
  }

  /* ---------- Front side ---------- */
  .card--front {
    left: 620px;
    background: linear-gradient(160deg, var(--card-dark) 0%, #353638 45%, var(--card-darker) 100%);
  }
  .front__mark {
    position: absolute;
    left: 12px; top: 22px;
    width: 230px; height: 230px;
  }
  .front__identity {
    position: absolute;
    left: 250px; right: 10px; top: 78px;
    text-align: center;
    color: var(--text-light);
  }
  .front__business {
    font-weight: 400;
    font-size: 25px;
    line-height: 31px;
  }
  .front__name {
    margin-top: 14px;
    font-size: 17px;
    line-height: 22px;
  }
  .front__role { font-size: 10px; }
  .front__quals {
    margin-top: 6px;
    font-size: 9.5px;
    color: var(--text-muted);
  }
  .front__rule {
    position: absolute;
    left: 0; right: 0; top: 244px;
    height: 2px;
    background: var(--gold-bright);
  }
  .front__contact {
    position: absolute;
    left: 0; right: 0; top: 258px;
    text-align: center;
    color: var(--text-light);
    font-style: italic;
    font-size: 9.5px;
    line-height: 14px;
  }
</style>
</head>
<body>

  <section class="card card--back" aria-label="Appointment card, reverse side">
    <header class="back__header">
      <span class="back__tab"></span>
      <h2 class="back__title">Appointment details</h2>
      <span class="back__bar"></span>
    </header>
    <ul class="back__fields">
      <li>Next appointment :</li>
      <li>Date :</li>
      <li>Time :</li>
    </ul>
    <footer class="back__footer">For more details please visit : www. tallowmind-example.com</footer>
  </section>

  <section class="card card--front" aria-label="Business card, front side">
    <svg class="front__mark" viewBox="0 0 230 230" aria-hidden="true">
      <circle cx="115" cy="115" r="108" fill="none" stroke="var(--gold)" stroke-width="4"/>
    </svg>
    <div class="front__identity">
      <h1 class="front__business">Meridian<br>Counselling Group</h1>
      <p class="front__name">Delia Farrant <span class="front__role">(FNBT Psychologist)</span></p>
      <p class="front__quals">BSc, Grad Dip Ed, M Psych (Clinical)</p>
    </div>
    <div class="front__rule"></div>
    <address class="front__contact">
      PO Box 714 Kellbrook SA 5291&nbsp; Mob: 0431 957 284 fax: 0869 413 508<br>
      Email: delia@tallowmind-example.com
    </address>
  </section>

</body>
</html>
```